Velantor corporate website

Dear graphic designers,
We would like to create a brand new corporate website for our company named "Velantor".
Velantor is a small Swiss premium IT company, with very prestigious clients in the Private Banking industry.
Here would be the values which could be associated to Velantor: trustworthy, serious, modern, high tech, high quality, sobriety, elegant.
Please find attached the Velantor logo in SVG format.
Our new website will have for only purpose to present briefly the company in one page: the team of experts (4 employees), the mission, the expertise and the contact info.
Very short and concise, easy to read.
Like this website for example but even shorter: https://www.mirdalex.example/

```html
<!DOCTYPE html>
<html lang="en">
<head>
<meta charset="utf-8">
<title>Velantor – Swiss premium IT company</title>
<link href="https://fonts.googleapis.com/css2?family=Poppins:wght@400;500;600;700;800&display=swap" rel="stylesheet">
<style>
:root{
  --blue:#1158aa;
  --blue-dark:#0c4a93;
  --ink:#0a0a0a;
  --text:#4a4a4a;
  --grey-band:#f0f0f0;
  --dark:#151515;
  --white:#ffffff;
  --illus-light:#dbe8fb;
}
*{box-sizing:border-box;margin:0;padding:0}
html,body{width:1200px;height:2667px;overflow:hidden;background:var(--white);font-family:'Poppins',sans-serif;color:var(--ink)}
.page{position:relative;width:1200px;height:2667px;overflow:hidden}
.abs{position:absolute}
.brand{font-family:'Poppins',sans-serif;font-weight:600;color:var(--blue);letter-spacing:1px;display:flex;align-items:center;gap:10px}
.brand-dot{width:14px;height:14px;border-radius:50%;background:var(--blue)}
.site-header .brand{left:82px;top:12px;font-size:34px}
.nav{display:flex;align-items:center;font-size:16px}
.site-header .nav{right:82px;top:13px}
.nav a{color:var(--ink);text-decoration:none;margin-left:48px}
.nav a.active{color:var(--blue)}
.nav .btn-contact{background:var(--blue);color:var(--white);border-radius:12px;padding:7px 20px;margin-left:30px}
.wave{position:absolute;left:0;width:1200px}
.hero-title{left:80px;top:178px;color:var(--white);font-size:44px;font-weight:700;line-height:46px;letter-spacing:.5px}
.hero-text{left:81px;top:290px;width:500px;color:var(--white);font-size:15px;line-height:24px}
.btn-outline{left:81px;top:362px;width:123px;height:37px;border:1px solid var(--blue);background:var(--white);border-radius:19px;color:var(--blue-dark);font-size:13px;font-weight:700;display:flex;align-items:center;justify-content:center}
.illus{border-radius:12px}
h2.section-title{position:absolute;font-size:40px;font-weight:700;letter-spacing:1px;color:var(--ink)}
.body-copy{font-size:16px;line-height:26px;color:var(--text);letter-spacing:.3px}
.btn-solid{background:var(--blue);color:var(--white);border-radius:19px;font-size:13px;font-weight:700;display:flex;align-items:center;justify-content:center}
.tile{position:absolute;width:160px;height:86px;background:var(--blue);border-radius:3px;display:flex;align-items:center;padding-left:14px;gap:14px;color:var(--white);font-size:14px;font-weight:600;line-height:20px}
.tile svg{flex:none}
.team-card{position:absolute;top:1667px;width:246px;height:215px;border-radius:10px;background:linear-gradient(180deg,var(--blue) 0%,#1d66b8 100%)}
.member-name{position:absolute;top:1893px;width:246px;text-align:center;color:var(--blue);font-weight:700;font-size:16px;letter-spacing:.5px}
.member-role{position:absolute;top:1920px;width:246px;text-align:center;color:var(--text);font-size:13px;letter-spacing:.5px}
.contact-band{left:0;top:1985px;width:1200px;height:395px;background:linear-gradient(110deg,#101010 0%,#2a2a2a 45%,#151515 100%)}
.field{position:absolute;background:var(--white);border-radius:3px;border:1px solid #ccc;font-size:14px;color:#666;padding:6px 10px;letter-spacing:.5px}
.footer-nav{top:2603px;left:0;width:1200px;justify-content:center;font-size:16px}
.footer-nav a{margin:0 36px}
.copyright{left:0;top:2643px;width:1200px;height:24px;background:#ececec;font-size:11px;color:#555;display:flex;align-items:center;justify-content:center}
</style>
</head>
<body>
<div class="page">

  <header class="site-header">
    <div class="abs brand"><span class="brand-dot"></span>VELANTOR</div>
    <nav class="abs nav">
      <a class="active" href="#team">Team</a>
      <a href="#mission">Mission</a>
      <a href="#expertise">Expertise</a>
      <a class="btn-contact" href="#contact">Contact</a>
    </nav>
  </header>

  <section class="hero">
    <svg class="wave" style="top:64px" height="460" viewBox="0 0 1200 460" preserveAspectRatio="none">
      <path d="M0 18 C250 -6 500 8 700 22 C900 36 1050 28 1200 12 L1200 442 C1050 455 900 462 700 448 C500 432 250 428 0 442 Z" fill="var(--blue)"/>
    </svg>
    <h1 class="abs hero-title">Velantor is a Swiss<br>premium IT company</h1>
    <p class="abs hero-text">Lorem ipsum dolor sit amet, consectetur adipiscing elit, sed do eiusmod tempor incididunt ut labore et dolore magna aliqua</p>
    <a class="abs btn-outline" href="#contact">Contact us</a>
    <div class="abs illus" role="img" aria-label="Illustration of a support agent with headset working at a desk with monitors" style="left:700px;top:115px;width:380px;height:395px;background:radial-gradient(ellipse at 60% 45%,#2a6fc0 0%,#1a4f9a 55%,rgba(17,88,170,0) 75%)"></div>
  </section>

  <section id="mission">
    <h2 class="section-title" style="left:80px;top:617px">Our Mission</h2>
    <p class="abs body-copy" style="left:81px;top:690px;width:495px">Lorem ipsum dolor sit amet, consectetur adipiscing elit, sed do eiusmod tempor incididunt ut labore et dolore magna aliqua. Ut enim ad minim veniam, quis nostrud exercitation ullamco laboris nisi ut aliquip ex ea commodo consequat. Duis aute irure dolor in reprehenderit in voluptate velit esse cillum dolore eu fugiat nulla pariatur.</p>
    <a class="abs btn-solid" href="#mission" style="left:81px;top:866px;width:123px;height:37px">Read More</a>
    <div class="abs illus" role="img" aria-label="Illustration of a woman at a laptop beside candidate profile cards and gears" style="left:655px;top:600px;width:463px;height:262px;background:radial-gradient(ellipse at 45% 50%,var(--illus-light) 0%,#e9f1fd 55%,rgba(255,255,255,0) 78%)"></div>
  </section>

  <section id="expertise">
    <svg class="wave" style="top:952px" height="460" viewBox="0 0 1200 460" preserveAspectRatio="none">
      <path d="M0 20 C200 -4 450 2 650 18 C850 34 1050 22 1200 16 L1200 455 C1000 445 800 432 600 440 C400 448 200 428 0 436 Z" fill="var(--grey-band)"/>
    </svg>
    <h2 class="section-title" style="left:78px;top:1030px">Expertise</h2>
    <p class="abs body-copy" style="left:80px;top:1101px;width:340px">Lorem ipsum dolor sit amet, consectetur adipiscing elit, sed do eiusmod tempor incididunt ut labore et dolore magna aliqua. Ut enim ad minim veniam, quis nostrud exercitation ullamco laboris nisi ut aliquip ex ea commodo consequat. Duis aute irure dolor</p>

    <div class="tile" style="left:440px;top:1106px">
      <svg width="38" height="38" viewBox="0 0 38 38"><path d="M16 8h16a4 4 0 0 1 4 4v8a4 4 0 0 1-4 4h-2l-4 4v-4" fill="none" stroke="#fff" stroke-width="2.5"/><ellipse cx="15" cy="23" rx="13" ry="10" fill="#fff"/><circle cx="10" cy="23" r="1.8" fill="var(--blue)"/><circle cx="15" cy="23" r="1.8" fill="var(--blue)"/><circle cx="20" cy="23" r="1.8" fill="var(--blue)"/></svg>
      <span>Corvanta<br>Consulting</span></div>
    <div class="tile" style="left:614px;top:1106px">
      <svg width="38" height="38" viewBox="0 0 38 38"><rect x="20" y="3" width="9" height="16" rx="2" transform="rotate(40 24 11)" fill="#fff"/><rect x="6" y="16" width="13" height="17" rx="2" transform="rotate(40 12 24)" fill="#fff"/></svg>
      <span>Data<br>Wiping</span></div>
    <div class="tile" style="left:787px;top:1106px">
      <svg width="38" height="38" viewBox="0 0 38 38"><circle cx="19" cy="19" r="18" fill="#fff"/><line x1="12" y1="26" x2="26" y2="12" stroke="var(--blue)" stroke-width="2.5"/><circle cx="13" cy="13" r="3" fill="none" stroke="var(--blue)" stroke-width="2.2"/><circle cx="25" cy="25" r="3" fill="none" stroke="var(--blue)" stroke-width="2.2"/></svg>
      <span>Negative<br>Interest</span></div>
    <div class="tile" style="left:960px;top:1106px">
      <svg width="38" height="38" viewBox="0 0 38 38"><rect x="2" y="6" width="34" height="22" fill="#fff"/><rect x="14" y="30" width="10" height="3" fill="#fff"/></svg>
      <span>Corvanta<br>Front Portal</span></div>

    <div class="tile" style="left:440px;top:1210px">
      <svg width="38" height="38" viewBox="0 0 38 38"><circle cx="19" cy="19" r="18" fill="#fff"/><circle cx="18" cy="18" r="6" fill="none" stroke="var(--blue)" stroke-width="2.5"/><line x1="22" y1="22" x2="26" y2="26" stroke="var(--blue)" stroke-width="2.5"/></svg>
      <span>Kestra 21</span></div>
    <div class="tile" style="left:614px;top:1210px">
      <svg width="46" height="38" viewBox="0 0 46 38"><rect x="2" y="10" width="42" height="20" rx="2" fill="none" stroke="#fff" stroke-width="2"/><rect x="6" y="6" width="38" height="4" fill="#fff" opacity=".7"/><circle cx="23" cy="20" r="6" fill="none" stroke="#fff" stroke-width="2"/><text x="23" y="24" font-size="9" font-family="Poppins,sans-serif" text-anchor="middle" fill="#fff">$</text></svg>
      <span>Instant<br>Payments</span></div>
    <div class="tile" style="left:787px;top:1210px">
      <svg width="38" height="38" viewBox="0 0 38 38"><path d="M8 30V14m5 16V8m5 22V8m5 14V12" stroke="#fff" stroke-width="3" stroke-linecap="round"/><circle cx="26" cy="28" r="6" fill="#fff"/><path d="M23.5 25.5l5 5m0-5l-5 5" stroke="var(--blue)" stroke-width="1.8"/></svg>
      <span>Sanctioned<br>Assets</span></div>
    <div class="tile" style="left:960px;top:1210px">
      <svg width="42" height="38" viewBox="0 0 42 38"><path d="M30 12H12a5 5 0 0 0 0 10h18a5 5 0 0 1 0 10H10" fill="none" stroke="#fff" stroke-width="2.5"/><rect x="30" y="9" width="8" height="6" rx="1" fill="#fff"/><rect x="4" y="29" width="8" height="6" rx="1" fill="#fff"/></svg>
      <span>Corvanta<br>CAPI</span></div>
  </section>

  <section id="team">
    <h2 class="section-title" style="left:0;width:1200px;text-align:center;top:1490px">Our Team</h2>
    <p class="abs" style="left:0;width:1200px;top:1550px;text-align:center;font-size:16px;color:#222;letter-spacing:.3px">Lorem ipsum dolor sit amet, consectetur adipiscing elit, sed do eiusmod tempor</p>

    <div class="team-card" role="img" aria-label="Portrait photo of team member in light blue shirt" style="left:83px"></div>
    <div class="team-card" role="img" aria-label="Portrait photo of team member in black shirt" style="left:348px"></div>
    <div class="team-card" role="img" aria-label="Portrait photo of team member in grey blazer" style="left:610px"></div>
    <div class="team-card" role="img" aria-label="Portrait photo of team member in denim shirt" style="left:873px"></div>

    <div class="member-name" style="left:78px">Marek Holm</div><div class="member-role" style="left:83px">CEO</div>
    <div class="member-name" style="left:347px">Tobin</div><div class="member-role" style="left:348px">CMO</div>
    <div class="member-name" style="left:606px">Ansel</div><div class="member-role" style="left:610px">TECHNICAL SUPERVISOR</div>
    <div class="member-name" style="left:868px">Marek Holm</div><div class="member-role" style="left:873px">CEOO</div>
  </section>

  <section id="contact">
    <div class="abs contact-band" role="img" aria-label="Dark background photo of a person wearing a headset"></div>
    <h2 class="section-title" style="left:0;width:1200px;text-align:center;top:2030px;color:var(--white);font-size:38px">Get In Touch</h2>
    <div class="field" style="left:403px;top:2109px;width:192px;height:30px">Name</div>
    <div class="field" style="left:603px;top:2109px;width:192px;height:30px">Last Name</div>
    <div class="field" style="left:403px;top:2147px;width:193px;height:32px">Phone Number</div>
    <div class="field" style="left:603px;top:2147px;width:194px;height:32px">Email</div>
    <div class="field" style="left:403px;top:2189px;width:395px;height:95px;padding-top:10px">Your Message Here</div>
    <a class="abs btn-solid" href="#contact" style="left:550px;top:2307px;width:101px;height:36px">Submit</a>
  </section>

  <footer>
    <div class="abs brand" style="left:0;width:1200px;justify-content:center;top:2418px;font-size:34px"><span class="brand-dot"></span>VELANTOR</div>
    <p class="abs" style="left:0;width:1200px;top:2477px;text-align:center;font-size:16px;line-height:22px;color:#555">Velantor 48 Lindenweg<br>Eastbrook</p>
    <div class="abs" style="left:414px;top:2544px;display:flex;align-items:center;gap:14px;font-size:16px;color:#555">
      <svg width="32" height="32" viewBox="0 0 32 32"><circle cx="16" cy="16" r="16" fill="var(--blue)"/><path d="M11 9l3 0 1.5 4-2 1.5a9 9 0 0 0 4 4l1.5-2 4 1.5v3a2 2 0 0 1-2 2A13 13 0 0 1 9 11a2 2 0 0 1 2-2z" fill="#fff"/></svg>
      <span>0445550192</span>
      <svg style="margin-left:8px" width="32" height="32" viewBox="0 0 32 32"><circle cx="16" cy="16" r="16" fill="var(--blue)"/><circle cx="16" cy="16" r="6" fill="none" stroke="#fff" stroke-width="2.5"/></svg>
      <span>Find Us On Our Network</span>
    </div>
    <nav class="abs nav footer-nav">
      <a href="#team">Team</a><a href="#mission">Mission</a><a href="#expertise">Expertise</a><a href="#contact">Contact</a>
    </nav>
    <div class="abs copyright">Copyright&nbsp; Velantor. All rights reserved &nbsp;|&nbsp; Term of Conditions &nbsp;privacy policy</div>
  </footer>

</div>
</body>
</html>
```